Bar and Grill needs specials signage

I have attached a file called "daily specials" I need it changed - so there is 1 sign/poster for each day/special
also attached other items to show some styling. I want the new posters chalkboard format, styled along the lines of the drink designs attached.
The designs should be scaleable, and editable, I will print locally

```html
<!DOCTYPE html>
<html lang="en">
<head>
<meta charset="utf-8">
<title>Daily Specials – Friday</title>
<link href="https://fonts.googleapis.com/css2?family=Cabin+Sketch:wght@400;700&family=Kaushan+Script&family=Gochi+Hand&display=swap" rel="stylesheet">
<style>
  :root {
    --board-dark: #272d29;
    --board-mid: #3a403c;
    --board-light: #575c58;
    --chalk-white: #f4f4f0;
    --chalk-blue: #5cc3ea;
    --chalk-yellow: #d9a22b;
    --chalk-faint: rgba(244, 244, 240, 0.12);
  }
  * { margin: 0; padding: 0; box-sizing: border-box; }
  html, body { width: 927px; height: 1200px; overflow: hidden; background: var(--board-dark); }
  .poster {
    position: relative;
    width: 927px;
    height: 1200px;
    overflow: hidden;
    background:
      radial-gradient(ellipse 45% 30% at 50% 62%, var(--board-light) 0%, transparent 100%),
      radial-gradient(ellipse 70% 55% at 50% 48%, var(--board-mid) 0%, var(--board-dark) 100%);
    color: var(--chalk-white);
  }
  .frame {
    position: absolute;
    inset: 32px;
    border: 4px solid var(--chalk-white);
    border-radius: 3px;
    opacity: 0.92;
  }
  .corner {
    position: absolute;
    width: 46px;
    height: 46px;
    background: var(--chalk-faint);
    border-radius: 50%;
  }
  .corner.tl { left: 36px; top: 24px; }
  .corner.tr { right: 36px; top: 24px; }
  .corner.bl { left: 36px; bottom: 24px; }
  .corner.br { right: 36px; bottom: 24px; }
  .heading {
    position: absolute;
    top: 82px;
    left: 0;
    width: 100%;
    text-align: center;
    font-family: "Cabin Sketch", cursive;
    font-weight: 400;
    font-size: 74px;
    letter-spacing: 2px;
    line-height: 1;
  }
  .day {
    position: absolute;
    top: 160px;
    left: 0;
    width: 100%;
    text-align: center;
    font-family: "Kaushan Script", cursive;
    font-size: 200px;
    line-height: 1.1;
  }
  .special-name {
    position: absolute;
    top: 520px;
    left: 0;
    width: 100%;
    text-align: center;
    font-family: "Cabin Sketch", cursive;
    font-weight: 700;
    font-size: 72px;
    letter-spacing: 4px;
    color: var(--chalk-blue);
    line-height: 1;
  }
  .rule {
    position: absolute;
    height: 4px;
    background: var(--chalk-white);
    border-radius: 2px;
  }
  .rule.r1 { left: 176px; width: 596px; top: 438px; }
  .rule.r2 { left: 152px; width: 436px; top: 468px; }
  .rule.r3 { left: 152px; width: 436px; top: 496px; }
  .rule.r4 { left: 152px; width: 620px; top: 608px; }
  .artwork {
    position: absolute;
    left: 196px;
    top: 640px;
    width: 526px;
    height: 320px;
    background: radial-gradient(ellipse at 50% 55%, rgba(244,244,240,0.22), rgba(244,244,240,0.04) 75%);
    border-radius: 40% 30% 30% 40%;
  }
  .accents { position: absolute; inset: 0; width: 927px; height: 1200px; }
  .description {
    position: absolute;
    top: 980px;
    left: 0;
    width: 100%;
    text-align: center;
    font-family: "Gochi Hand", cursive;
    font-size: 56px;
    line-height: 1.1;
    letter-spacing: 1px;
  }
</style>
</head>
<body>
<main class="poster">
  <div class="frame"></div>
  <div class="corner tl" role="img" aria-label="Chalk flourish ornament"></div>
  <div class="corner tr" role="img" aria-label="Chalk flourish ornament"></div>
  <div class="corner bl" role="img" aria-label="Chalk flourish ornament"></div>
  <div class="corner br" role="img" aria-label="Chalk flourish ornament"></div>

  <h1 class="heading">DAILY SPECIALS</h1>
  <h2 class="day">Friday</h2>

  <div class="rule r1"></div>
  <div class="rule r2"></div>
  <div class="rule r3"></div>

  <p class="special-name">FISH AND CHIPS</p>
  <div class="rule r4"></div>

  <div class="artwork" role="img" aria-label="Chalk sketch of a fish beside a basket of chips"></div>

  <svg class="accents" viewBox="0 0 927 1200" aria-hidden="true">
    <g stroke="var(--chalk-yellow)" stroke-width="3" stroke-linecap="round" fill="none">
      <line x1="104" y1="206" x2="142" y2="218"/>
      <line x1="88" y1="282" x2="130" y2="282"/>
      <line x1="100" y1="356" x2="138" y2="350"/>
      <line x1="792" y1="218" x2="830" y2="206"/>
      <line x1="806" y1="282" x2="848" y2="282"/>
      <line x1="798" y1="350" x2="836" y2="356"/>
    </g>
    <g stroke="var(--chalk-yellow)" stroke-width="3" stroke-linejoin="round" fill="rgba(217,162,43,0.18)">
      <path d="M110 842 L126 832 L162 890 L172 884 L174 930 L136 910 L146 904 Z"/>
      <path d="M818 646 L826 662 L772 702 L780 712 L740 732 L752 690 L760 698 Z"/>
    </g>
  </svg>

  <p class="description">Beer battered cod fish<br>and steak fries</p>
</main>
</body>
</html>
```